Business Card needed for Drainor, a growing Septic Service company

Drainor, a growing local septic service company in Pennsylvania, needs updated business cards. We'd like the business card to feature our logo and communicate that we provide Septic Pumping, Installations/Repairs, Restroom Rentals, and 24/7 Emergency Service. The business card should be eye-catching, bold, and clean/simple. We have been in business almost 10 years and would like to expand and update our business brand and image.

Target Market(s)

Residential and Commercial, New and Current Homeowners

Industry/Entity Type

Service

Contact Information for Business Card

Contact on the business card should be: Dean Harlow Owner & Operator
Phone: 555-555-0187
Email: service@drainor-example.com
Website: www.drainor-example.com
Address: 812 Millbrook Lane Alderton NA 00042

Font styles to use
Sans Serif

Colors

Designer to choose colors to be used in the design.

Requirements
Must have
• Feature logo on both side of business card.
Nice to have
• We envision the contact information on one side and our services listed on the other side. Utilize the green from the symbol in our logo as part of the design, overall design color scheme should be white, grey, black.

```html
<!DOCTYPE html>
<html lang="en">
<head>
<meta charset="utf-8">
<title>Drainor Business Card</title>
<link rel="stylesheet" href="https://fonts.googleapis.com/css2?family=Montserrat:wght@400;500;600;800&display=swap">
<style>
  :root {
    --backdrop: #eef0ea;
    --brand-green: #86c240;
    --ink: #1d1d1b;
    --paper: #ffffff;
    --rule: #3a3a3a;
  }
  * { margin: 0; padding: 0; box-sizing: border-box; }
  html, body {
    width: 1200px; height: 579px; overflow: hidden;
    background: var(--backdrop);
    font-family: "Montserrat", sans-serif;
    color: var(--ink);
  }
  .stage { position: relative; width: 1200px; height: 579px; }
  .card {
    position: absolute; top: 146px;
    width: 428px; height: 244px; overflow: hidden;
  }
  .card--front { left: 142px; background: var(--paper); }
  .card--back { left: 634px; background: var(--brand-green); }

  /* Front */
  .brand-square {
    position: absolute; left: 100px; top: 76px;
    width: 36px; height: 36px; background: var(--brand-green);
  }
  .brand-name {
    position: absolute; left: 145px; top: 72px;
    font-weight: 800; font-size: 34px; letter-spacing: 1.5px;
    line-height: 44px; color: var(--ink); white-space: nowrap;
  }
  .services {
    position: absolute; top: 130px; list-style: none;
    font-size: 10px; font-weight: 500; white-space: nowrap;
  }
  .services li { line-height: 13px; padding: 3px 0; }
  .services li:first-child { border-bottom: 1px solid var(--rule); }
  .services--left { left: 84px; width: 113px; text-align: right; }
  .services--right { left: 231px; width: 128px; }
  .services-divider {
    position: absolute; left: 213px; top: 131px;
    width: 1px; height: 36px; background: var(--ink);
  }

  /* Back */
  .brand-mark {
    position: absolute; left: 239px; top: -50px;
    width: 230px; height: 230px; border-radius: 50%;
    background: var(--paper);
    display: flex; align-items: center; justify-content: center;
  }
  .brand-mark span {
    font-weight: 800; font-size: 24px; letter-spacing: 1px; color: var(--ink);
    margin-left: -20px; margin-top: 40px;
  }
  .holder-name {
    position: absolute; left: 30px; top: 44px;
    font-weight: 600; font-size: 22px; line-height: 28px;
    padding-bottom: 5px; border-bottom: 1.5px solid var(--ink);
    white-space: nowrap;
  }
  .holder-title {
    position: absolute; left: 30px; top: 86px;
    font-weight: 500; font-size: 12.5px; white-space: nowrap;
  }
  .contacts {
    position: absolute; left: 30px; top: 128px; list-style: none;
    font-size: 10.5px; white-space: nowrap;
  }
  .contacts li { display: flex; align-items: center; height: 19px; }
  .contacts svg { width: 11px; height: 11px; margin-right: 8px; fill: var(--ink); flex: none; }
</style>
</head>
<body>
<main class="stage">
  <section class="card card--front" aria-label="Card front">
    <div class="brand-square"></div>
    <div class="brand-name">DRAINOR</div>
    <ul class="services services--left">
      <li>Septic Pumping</li>
      <li>Installations / Repairs</li>
    </ul>
    <div class="services-divider"></div>
    <ul class="services services--right">
      <li>Restroom Rentals</li>
      <li>24/7 Emergency Service</li>
    </ul>
  </section>

  <section class="card card--back" aria-label="Card back">
    <div class="brand-mark"><span>DRAINOR</span></div>
    <h1 class="holder-name">Dean Harlow</h1>
    <p class="holder-title">Owner &amp; Operator</p>
    <ul class="contacts">
      <li><svg viewBox="0 0 24 24"><path d="M6.6 10.8c1.4 2.8 3.8 5.1 6.6 6.6l2.2-2.2c.3-.3.7-.4 1-.2 1.1.4 2.3.6 3.6.6.6 0 1 .4 1 1V20c0 .6-.4 1-1 1C10.6 21 3 13.4 3 4c0-.6.4-1 1-1h3.5c.6 0 1 .4 1 1 0 1.3.2 2.5.6 3.6.1.3 0 .7-.2 1z"/></svg>555-555-0187</li>
      <li><svg viewBox="0 0 24 24"><path d="M12 3 2 12h3v9h5v-6h4v6h5v-9h3z"/></svg>service@drainor-example.com</li>
      <li><svg viewBox="0 0 24 24"><path d="M12 2a10 10 0 1 0 0 20 10 10 0 0 0 0-20zm6.9 9h-3a15 15 0 0 0-1.3-6 8 8 0 0 1 4.3 6zM12 4c.9 1.3 1.7 3.9 1.9 7h-3.8c.2-3.1 1-5.700 1.9-7zM9.4 5a15 15 0 0 0-1.3 6h-3a8 8 0 0 1 4.3-6zM5.1 13h3a15 15 0 0 0 1.3 6 8 8 0 0 1-4.300-6zM12 20c-.9-1.3-1.700-3.9-1.9-7h3.8c-.2 3.1-1 5.7-1.9 7zm2.6-1a15 15 0 0 0 1.3-6h3a8 8 0 0 1-4.3 6z"/></svg>www.drainor-example.com</li>
      <li><svg viewBox="0 0 24 24"><path d="M2 5h20v14H2zm2 2v.5l8 5 8-5V7z"/></svg>812 Millbrook Lane Alderton NA 00042</li>
    </ul>
  </section>
</main>
</body>
</html>
```